Torvik Apparel Brochure Project

Looking for a brochure to send out with samples of our apparel. The name of our company is Torvik Apparel and we are distributors for 7.42. I have attached an older 7.42 brochure. I would like the brochure to be regular paper size with no folds.

Target Market(s)

Buyers working for large U.S. retail stores

Colors

Designer to choose colors to be used in the design.

Requirements
Must have
• Must look sleek and professional.

```html
<!DOCTYPE html>
<html lang="en">
<head>
<meta charset="utf-8">
<title>Torvik Apparel Brochure</title>
<link href="https://fonts.googleapis.com/css2?family=Lato:wght@400;700&display=swap" rel="stylesheet">
<style>
:root{
  --board-light:#d1d3d4;
  --board-dark:#3c3c3e;
  --red:#d81f26;
  --red-deep:#8f1a1c;
  --paper:#ffffff;
  --paper-grey:#eef0f1;
  --ink:#2b2b2b;
  --white:#ffffff;
}
*{margin:0;padding:0;box-sizing:border-box}
html,body{width:1200px;height:2419px;overflow:hidden}
body{
  font-family:"Lato",Arial,sans-serif;
  background:linear-gradient(to bottom,var(--board-light) 0,var(--board-light) 2056px,var(--board-dark) 2056px);
  position:relative;
}
.page{position:absolute;width:404px;height:521px;background:var(--paper);box-shadow:6px 8px 14px rgba(0,0,0,.35);overflow:hidden}
.swoosh{position:absolute;left:0;width:404px}
.swoosh--top{top:0;height:120px}
.swoosh--bottom{bottom:0;height:110px}

/* cover letter */
.letter{left:398px;top:100px}
.letter__mark{position:absolute;left:0;right:0;top:44px;text-align:center;z-index:2}
.mark-dot{display:inline-block;width:84px;height:84px;border-radius:50%;background:var(--red-deep);border:4px solid var(--white);box-shadow:0 0 0 2px var(--red-deep)}
.letter__name{display:block;margin-top:6px;font-size:13px;font-weight:700;color:var(--red-deep);letter-spacing:.5px}
.letter__body{position:absolute;left:32px;top:188px;width:342px;font-size:8.1px;line-height:1.38;color:var(--ink)}
.letter__body p{margin-bottom:8px}
.letter__body p.letter__closing{margin-top:16px}
.letter__address{position:absolute;right:30px;top:462px;text-align:right;font-size:10px;line-height:1.3;color:var(--red-deep);z-index:2}

/* lookbook pages */
.look{background:linear-gradient(to bottom,var(--paper) 0,var(--paper-grey) 100%)}
.look__mark{position:absolute;left:12px;top:36px;display:flex;align-items:center;gap:6px}
.look__dot{width:40px;height:40px;border-radius:50%;background:var(--red-deep);border:3px solid var(--white);box-shadow:0 0 0 1.5px var(--red-deep)}
.look__name{font-size:10px;font-weight:700;color:var(--red-deep);margin-top:22px}
.photo{position:absolute;border-radius:10px}
.photo--main{left:165px;top:90px;width:236px;height:397px}
.photo--upper{left:31px;top:187px;width:122px;height:145px}
.photo--lower{left:31px;top:343px;width:122px;height:144px}
.look--a{left:184px;top:665px}
.look--b{left:615px;top:665px}
.look--c{left:184px;top:1231px}
.look--d{left:615px;top:1231px}
.look--a .photo{background:linear-gradient(160deg,#6f6a4c,#9b7558 55%,#5d4a38)}
.look--b .photo{background:linear-gradient(160deg,#4b6a3a,#2c3a5c 55%,#7c8376)}
.look--c .photo{background:linear-gradient(160deg,#4f5a3a,#3c4f8c 55%,#a89a83)}
.look--d .photo{background:linear-gradient(160deg,#55603d,#d9d6cc 55%,#6b5e45)}

/* back cover */
.back{left:398px;top:1798px;background:var(--red-deep);color:var(--white);text-align:center}
.back__mark{position:absolute;left:102px;top:18px;width:200px;height:200px;border-radius:50%;border:4px solid var(--white)}
.back__name{position:absolute;left:0;right:0;top:236px;font-size:18px;font-weight:700}
.back__intro{position:absolute;left:0;right:0;top:378px;font-size:9.5px;line-height:1.3}
.back__contact{position:absolute;left:0;right:0;top:438px;font-size:13px;line-height:1.25;font-weight:700}
.back__address{position:absolute;left:0;right:0;top:482px;font-size:8.5px}
</style>
</head>
<body>

<svg width="0" height="0" style="position:absolute" aria-hidden="true">
  <defs>
    <linearGradient id="redband" x1="0" y1="0" x2="1" y2="0">
      <stop offset="0" stop-color="#8f1a1c"/><stop offset=".5" stop-color="#d81f26"/><stop offset="1" stop-color="#e8343a"/>
    </linearGradient>
  </defs>
</svg>

<section class="page letter">
  <svg class="swoosh swoosh--top" viewBox="0 0 404 120" preserveAspectRatio="none" aria-hidden="true">
    <path d="M0 0H404V28C300 40 180 60 0 74Z" fill="url(#redband)"/>
    <path d="M0 80C150 62 290 44 404 36V44C290 52 160 72 0 90Z" fill="#d81f26" opacity=".55"/>
    <path d="M0 96C170 74 300 60 404 56" stroke="#dcdcdc" stroke-width="3" fill="none"/>
  </svg>
  <div class="letter__mark"><span class="mark-dot"></span><span class="letter__name">Torvik Apparel</span></div>
  <div class="letter__body">
    <p>We proudly present the finest artisanal luxury, hand-spun and hand-woven (known as "khadi") fabric products, emphasizing the link between farmers, weavers, vegetable dyes and block printing traditions. This result is a coherent and meaningful fashion garment-line that creates grounds for ethical products.</p>
    <p>Our clothes are 100% handmade by 7.42/seven forty-two artisans and we select the finest of fabrics for our designs including khadi denim, kala cotton (all organic), 100 count khadi cotton, silk and ahimsa silk. All cotton fabric used by 7.42/seven forty-two is 100% khadi cotton and dyed in 100% natural dyes.</p>
    <p>Khadi is an ideal choice for green and ethical clothing. Made from cotton, silk, wool and other natural fibers, these fabrics have been in existence for hundreds of years. Today the production of khadi provides sustenance to millions of people in India. About eighty percent of khadi artisans are women; often from some of the poorest communities in the country.</p>
    <p>Our fabric simply looks beautiful. It is a labor of love. It's about human beings working with nature and transforming natural materials into beautiful wearable clothing.</p>
    <p class="letter__closing">We would love to talk with you about supplying our artisan products to your establishment. Please feel free to contact me via email at hello@torvikapparel.com or cell phone at 555-014-2290.</p>
  </div>
  <svg class="swoosh swoosh--bottom" viewBox="0 0 404 110" preserveAspectRatio="none" aria-hidden="true">
    <path d="M0 8C120 40 260 84 404 100V110H0Z" fill="url(#redband)"/>
    <path d="M0 0C140 30 280 72 404 88" stroke="#e4e4e4" stroke-width="4" fill="none"/>
  </svg>
  <div class="letter__address">48 Harbor Crest Lane,<br>Fairmont Hills, CA 91400</div>
</section>

<section class="page look look--a">
  <svg class="swoosh swoosh--top" viewBox="0 0 404 120" preserveAspectRatio="none" aria-hidden="true">
    <path d="M0 0H404V4C280 12 150 24 0 46Z" fill="url(#redband)"/>
    <path d="M40 44C170 22 300 12 404 10" stroke="#d81f26" stroke-width="2" fill="none"/>
  </svg>
  <div class="look__mark"><span class="look__dot"></span><span class="look__name">Torvik Apparel</span></div>
  <div class="photo photo--upper" role="img" aria-label="Model in a printed sleeveless maxi dress by a pool"></div>
  <div class="photo photo--lower" role="img" aria-label="Back view of the printed maxi dress"></div>
  <div class="photo photo--main" role="img" aria-label="Model wearing a patterned khadi maxi dress among rocks"></div>
</section>

<section class="page look look--b">
  <svg class="swoosh swoosh--top" viewBox="0 0 404 120" preserveAspectRatio="none" aria-hidden="true">
    <path d="M0 0H404V4C280 12 150 24 0 46Z" fill="url(#redband)"/>
    <path d="M40 44C170 22 300 12 404 10" stroke="#d81f26" stroke-width="2" fill="none"/>
  </svg>
  <div class="look__mark"><span class="look__dot"></span><span class="look__name">Torvik Apparel</span></div>
  <div class="photo photo--upper" role="img" aria-label="Model in a navy sleeveless dress in a garden"></div>
  <div class="photo photo--lower" role="img" aria-label="Side view of the navy sleeveless dress"></div>
  <div class="photo photo--main" role="img" aria-label="Model wearing a navy khadi denim shift dress on a garden path"></div>
</section>

<section class="page look look--c">
  <svg class="swoosh swoosh--top" viewBox="0 0 404 120" preserveAspectRatio="none" aria-hidden="true">
    <path d="M0 0H404V4C280 12 150 24 0 46Z" fill="url(#redband)"/>
    <path d="M40 44C170 22 300 12 404 10" stroke="#d81f26" stroke-width="2" fill="none"/>
  </svg>
  <div class="look__mark"><span class="look__dot"></span><span class="look__name">Torvik Apparel</span></div>
  <div class="photo photo--upper" role="img" aria-label="Back view of a blue long-sleeve dress"></div>
  <div class="photo photo--lower" role="img" aria-label="Model in the blue long-sleeve dress beside a pool"></div>
  <div class="photo photo--main" role="img" aria-label="Model wearing a blue long-sleeve khadi dress with sunglasses"></div>
</section>

<section class="page look look--d">
  <svg class="swoosh swoosh--top" viewBox="0 0 404 120" preserveAspectRatio="none" aria-hidden="true">
    <path d="M0 0H404V4C280 12 150 24 0 46Z" fill="url(#redband)"/>
    <path d="M40 44C170 22 300 12 404 10" stroke="#d81f26" stroke-width="2" fill="none"/>
  </svg>
  <div class="look__mark"><span class="look__dot"></span><span class="look__name">Torvik Apparel</span></div>
  <div class="photo photo--upper" role="img" aria-label="Back view of a white sleeveless dress"></div>
  <div class="photo photo--lower" role="img" aria-label="Front view of the white sleeveless dress"></div>
  <div class="photo photo--main" role="img" aria-label="Model wearing a white khadi cotton slip dress in a garden"></div>
</section>

<section class="page back">
  <div class="back__mark"></div>
  <div class="back__name">Torvik Apparel</div>
  <p class="back__intro">We would love to talk with you about supplying<br>our artisan products to your establishment.<br>Please feel free to contact me via email at</p>
  <p class="back__contact">hello@torvikapparel.com or cell<br>phone at 555-014-2290.</p>
  <p class="back__address">48 Harbor Crest Lane, Fairmont Hills, CA 91400</p>
</section>

</body>
</html>
```